Wedding Decor and Entertianment business card

Company - We run a weddings and events company called Amber Fern, we provide most entertainment and decor services to our customers.

Initial idea is ....
A simple business card with logo on the front, this will be spot varnish. On a matt black background.
The reverse will be simple contact information.

But happy to try things outside of the box and would welcome some crazy ideas.

Target Market(s)

wedding couples - 21 - 40
High end wedding venues.

Industry/Entity Type

Wedding

Contact Information for Business Card

01742 918 263
amberfern.co.uk
rupert@amberfern.co.uk
or
eleanor@amberfern.co.uk

Requirements
Nice to have
• black matt background with spot varnish logo on the front.

```html
<!DOCTYPE html>
<html lang="en">
<head>
<meta charset="utf-8">
<title>Amber Fern — Business Card</title>
<link href="https://fonts.googleapis.com/css2?family=Jost:wght@400;600&display=swap" rel="stylesheet">
<style>
  :root {
    --backdrop: #7d7d7d;
    --card-slate: #22262b;
    --card-black: #1f2020;
    --plum: #7b4a70;
    --plum-soft: #9a7a94;
    --varnish: #2b2c2d;
    --varnish-edge: #3a3b3c;
  }
  html, body {
    margin: 0;
    width: 1200px;
    height: 1000px;
    overflow: hidden;
    background: var(--backdrop);
    font-family: "Jost", sans-serif;
  }
  .canvas {
    position: relative;
    width: 1200px;
    height: 1000px;
  }
  .card {
    position: absolute;
    box-shadow: 0 6px 14px rgba(0,0,0,0.35);
  }
  .card-front {
    left: 75px; top: 35px;
    width: 368px; height: 208px;
    background: var(--card-slate);
    display: flex;
    align-items: center;
    justify-content: center;
  }
  .brand-name {
    color: var(--plum);
    font-weight: 400;
    font-size: 22px;
    letter-spacing: 0.22em;
    text-transform: uppercase;
    margin: 0;
  }
  .card-back {
    left: 470px; top: 40px;
    width: 368px; height: 208px;
    background: var(--card-slate);
  }
  .pattern-strip {
    position: absolute;
    top: 0; left: 19px;
    width: 36px; height: 208px;
  }
  .contact {
    position: absolute;
    right: 24px; top: 72px;
    text-align: right;
    color: var(--plum);
  }
  .contact-name {
    margin: 0;
    font-weight: 600;
    font-size: 29px;
    letter-spacing: 0.12em;
    padding-bottom: 4px;
    border-bottom: 1px solid var(--plum);
    display: inline-block;
    padding-left: 6px;
  }
  .contact-lines {
    list-style: none;
    margin: 18px 0 0;
    padding: 0;
    font-size: 13.5px;
    letter-spacing: 0.12em;
    line-height: 17px;
  }
  .card-varnish {
    left: 100px; top: 320px;
    width: 1000px; height: 570px;
    background: var(--card-black);
    box-shadow: 0 10px 26px rgba(0,0,0,0.45);
    display: flex;
    align-items: center;
    justify-content: center;
  }
  .varnish-name {
    margin: 0;
    font-weight: 400;
    font-size: 60px;
    letter-spacing: 0.3em;
    text-transform: uppercase;
    color: var(--varnish);
    text-shadow: 0 1px 0 var(--varnish-edge), 0 -1px 0 #151515;
  }
</style>
</head>
<body>
  <main class="canvas">
    <section class="card card-front" aria-label="Card front">
      <h1 class="brand-name">Amber Fern</h1>
    </section>

    <section class="card card-back" aria-label="Card back">
      <svg class="pattern-strip" viewBox="0 0 36 208" role="img" aria-label="Two vertical interlaced braid ornament bands">
        <rect x="0" y="0" width="13" height="208" fill="var(--plum-soft)" opacity="0.55"/>
        <rect x="20" y="0" width="13" height="208" fill="var(--plum-soft)" opacity="0.55"/>
      </svg>
      <div class="contact">
        <h2 class="contact-name">John Doe</h2>
        <ul class="contact-lines">
          <li>01742 918 263</li>
          <li>amberfern.co.uk</li>
          <li>rupert@amberfern.co.uk</li>
        </ul>
      </div>
    </section>

    <section class="card card-varnish" aria-label="Spot varnish front">
      <h2 class="varnish-name">Amber Fern</h2>
    </section>
  </main>
</body>
</html>
```